Email Marketing Newsletter Design

Require the design of a email marketing newsletter. I will convert it into an updatable html template. I have supplied the copy for the first edition.

The newsletter is for a company that provides commercial property maintenance services such as office cleaning, lawns & gardens, electrical work etc

Web Site for client is:

http://brenvoli.com.au/cgi-bin/xmlweb.cgi/home/index_html
Updates

Hi Maud

I will upload the doc as a PDF.

The width needs to be 777px

Look forward to seeing your design

Rgds
Derek

Target Market(s)

Property Facility Managers and Maintenance Managers working for commerical office buildings and large corporate sites

Industry/Entity Type

Construction

Number of Pages Required

1 page

Requirements
Must have
• Must be 777px wide
• Strong branding

• Intro paragraph

• Monthly Specials section

• Service Feature section

• Simple but clean with strong design elements
Nice to have
• Send to a friend icon

```html
<!DOCTYPE html>
<html lang="en">
<head>
<meta charset="utf-8">
<title>Brenvoli Property Services Group Newsletter</title>
<link href="https://fonts.googleapis.com/css2?family=Open+Sans:wght@400;600;700&family=Arimo:wght@400;700&family=Tinos&display=swap" rel="stylesheet">
<style>
  :root {
    --navy: #0d3a80;
    --sky: #1d5bb0;
    --green: #a3c764;
    --green-light: #b9d77f;
    --green-dark: #82ad3b;
    --grey-panel: #e4e4e4;
    --grey-band: #3a3a3a;
    --ink: #1a1a1a;
    --heading-blue: #0d3a80;
    --white: #ffffff;
  }
  * { margin: 0; padding: 0; box-sizing: border-box; }
  html, body { width: 1080px; height: 1200px; overflow: hidden; background: var(--white); }
  body { font-family: "Open Sans", Arial, sans-serif; color: var(--ink); }

  .newsletter {
    position: relative;
    width: 900px; height: 1000px;
    transform: scale(1.2);
    transform-origin: 0 0;
    overflow: hidden;
    background: var(--white);
  }
  .layer { position: absolute; }

  /* header */
  .header-wave { left: 0; top: 0; width: 900px; height: 240px; }
  .brand { left: 30px; top: 22px; color: var(--white); }
  .brand-name {
    display: flex; align-items: center; gap: 16px;
    font-family: "Arimo", Arial, sans-serif; font-weight: 700;
    font-size: 76px; line-height: 1; letter-spacing: 4px;
  }
  .brand-mark { width: 58px; height: 58px; background: var(--white); }
  .brand-sub {
    position: absolute; left: 158px; top: 68px; white-space: nowrap;
    font-family: "Arimo", Arial, sans-serif; font-size: 25px;
  }
  .brand-issue {
    position: absolute; left: 240px; top: 92px;
    font-family: "Arimo", Arial, sans-serif; font-weight: 700; font-size: 43px;
  }
  .phone {
    left: 567px; top: 27px; color: var(--white); white-space: nowrap;
    font-family: "Arimo", Arial, sans-serif; font-weight: 700; font-size: 31px;
    text-shadow: 0 1px 2px rgba(0,0,0,.35);
  }
  .phone small { font-size: 25px; }
  .anniversary { left: 572px; top: 88px; width: 180px; height: 108px; color: var(--white); font-family: "Tinos", Georgia, serif; }
  .anniversary svg { position: absolute; inset: 0; }
  .anniversary-tag { position: absolute; left: 20px; top: 6px; width: 138px; text-align: center; font-size: 17px; letter-spacing: .5px; }
  .anniversary-years { position: absolute; left: 30px; top: 28px; display: flex; align-items: flex-start; }
  .anniversary-years b { font-weight: 400; font-size: 56px; line-height: 1; }
  .anniversary-years span { font-size: 30px; line-height: 1; margin-top: 6px; }
  .anniversary-years em { position: absolute; left: 76px; top: 38px; font-style: normal; font-size: 10px; white-space: nowrap; }

  /* side panel */
  .side-panel { left: 626px; top: 243px; width: 274px; height: 421px; background: var(--grey-panel); border-radius: 10px 0 0 10px; }
  .building-photo { left: 643px; top: 253px; width: 207px; height: 208px; background: linear-gradient(180deg, #1c5ec8 0%, #4c8ee0 45%, #a9c2d8 80%, #6f8f52 100%); }
  .news-box { left: 643px; top: 473px; width: 207px; height: 163px; background: linear-gradient(180deg, var(--green-light), var(--green-dark)); color: var(--white); padding: 14px 14px; border-radius: 0 0 6px 6px; overflow: hidden; }
  .news-box h3 { font-size: 21px; font-weight: 600; margin-bottom: 14px; }
  .news-box li { list-style: none; font-size: 16.5px; line-height: 23px; }
  .news-stripes { position: absolute; right: 0; bottom: 8px; width: 80px; height: 60px; }

  /* content boxes */
  .intro {
    left: 33px; top: 253px; width: 559px; height: 158px;
    background: var(--navy); color: var(--white); border-radius: 8px;
    padding: 16px 32px 16px 22px; font-size: 15.5px; line-height: 22px;
    box-shadow: 0 3px 5px rgba(0,0,0,.25);
  }
  .offer {
    left: 33px; top: 452px; width: 567px; height: 184px;
    border: 1px solid #333; border-radius: 8px; background: var(--white);
    padding: 24px 16px 0 10px; box-shadow: 0 3px 5px rgba(0,0,0,.2);
  }
  .offer h2 { color: var(--heading-blue); font-size: 17px; font-weight: 700; }
  .offer h4 { font-size: 17px; font-weight: 400; margin-bottom: 16px; }
  .offer p { font-size: 11.5px; line-height: 16px; }

  .band { left: 0; top: 770px; width: 900px; height: 100px; background: linear-gradient(180deg, #555 0%, var(--grey-band) 100%); }
  .spotlight {
    left: 33px; top: 676px; width: 827px; height: 162px;
    background: var(--navy); color: var(--white);
    border: 2px solid var(--white); border-radius: 8px;
    padding: 4px 30px 0 60px; box-shadow: 0 2px 6px rgba(0,0,0,.35);
  }
  .spotlight h2 { font-size: 20px; font-weight: 700; margin: 0 0 4px 10px; }
  .spotlight p { font-size: 11.6px; line-height: 17px; }
  .spotlight-lamp {
    left: 22px; top: 650px; width: 64px; height: 64px; border-radius: 50%;
    background: radial-gradient(circle at 40% 40%, #7a7a7a 0%, #3a3a3a 60%, #1e1e1e 100%);
  }

  /* footer */
  .footer-shape { left: 0; top: 850px; width: 900px; height: 150px; }
  .signoff { left: 60px; top: 897px; color: var(--white); }
  .signoff h2 { font-size: 32px; font-weight: 700; line-height: 1.15; }
  .signoff p { font-size: 15.5px; margin-left: 2px; }
  .contact { right: 33px; top: 920px; text-align: right; color: #333; }
  .contact .email { font-family: "Arimo", Arial, sans-serif; font-weight: 700; font-size: 18px; }
  .contact .web { font-family: "Arimo", Arial, sans-serif; font-size: 30px; color: #3a3a3a; }
  .footer-stripes { left: 755px; top: 815px; width: 145px; height: 80px; }
</style>
</head>
<body>
<main class="newsletter">

  <svg class="layer header-wave" viewBox="0 0 900 240" aria-hidden="true">
    <path d="M0 0 H900 V196 C850 215 790 230 700 222 C560 210 470 168 330 158 C200 150 100 160 0 164 Z" fill="#0d3a80"/>
    <path d="M600 216 C720 236 820 222 900 196" stroke="#1d5bb0" stroke-width="3" fill="none" opacity=".6"/>
  </svg>

  <div class="layer brand">
    <div class="brand-name"><span class="brand-mark"></span>BRENVOLI</div>
    <div class="brand-sub">Property Services Group</div>
    <div class="brand-issue">newsletter</div>
  </div>

  <div class="layer phone"><small>Call</small> 1300 58 41 70</div>

  <div class="layer anniversary">
    <svg viewBox="0 0 180 108" aria-hidden="true">
      <ellipse cx="90" cy="58" rx="88" ry="44" fill="none" stroke="#ffffff" stroke-width="1.5"/>
      <rect x="18" y="4" width="140" height="24" fill="#0d3a80" stroke="#ffffff" stroke-width="1.5"/>
    </svg>
    <div class="anniversary-tag">CELEBRATING</div>
    <div class="anniversary-years"><b>15</b><span>years</span><em>OF BUSINESS</em></div>
  </div>

  <div class="layer side-panel"></div>
  <div class="layer building-photo" role="img" aria-label="Photo of a modern curved glass office building against a blue sky"></div>

  <aside class="layer news-box">
    <h3>News / Links</h3>
    <ul>
      <li>&gt; Insert Link 1</li>
      <li>&gt; Insert Link 2</li>
      <li>&gt; Insert Link 3</li>
    </ul>
    <svg class="news-stripes" viewBox="0 0 80 60" aria-hidden="true">
      <g fill="#ffffff">
        <polygon points="10,8 80,0 80,10 10,18"/>
        <polygon points="6,24 80,16 80,26 6,34"/>
        <polygon points="14,40 80,32 80,42 14,50"/>
      </g>
    </svg>
  </aside>

  <section class="layer intro">
    <p><strong>Brenvoli</strong> is pleased to present our first e-newsletter. We believe in making life easier for our clients. So, we have created an e-newsletter to let you know about our current promotions and the services that we offer. Please enjoy learning about the range of ways Brenvoli can look after your office cleaning and maintenance needs.</p>
  </section>

  <section class="layer offer">
    <h2>December Offer:</h2>
    <h4>FREE Expert Brenvoli Carpet and Window Clean</h4>
    <p>At Brenvoli, we believe in rewarding our loyal customers. This month, we are offering a FREE carpet and window clean if you engage our standard office cleaning services for at least 6 months. There are no strings attached and no contracts to sign!<br>Call Brenvoli today and allow us to manage all of your cleaning needs for you!</p>
  </section>

  <div class="layer band"></div>

  <section class="layer spotlight">
    <h2>Spotlight: Brenvoli Cleaning Services</h2>
    <p>A Brenvoli office clean will look after all aspects of your office site. Our service includes regularly and thoroughly cleaning: floors, desks, kitchens and bathrooms. We also look after: window cleaning, carpet cleaning, vinyl floor stripping sealing, Venetian blind cleaning, floor sweeping, floor scrubbing, high pressure cleaning, ceiling tile and light cleaning and graffiti removal.<br>
    We realise that cleaning should be a background activity. You won’t notice we are there; you will notice that you don’t need to self manage the cleaning process, we do that for you.<br>
    Allow our experienced, expert staff to project manage all of your regular, and irregular, office cleaning needs!</p>
  </section>
  <div class="layer spotlight-lamp" role="img" aria-label="Illustration of a stage spotlight lamp"></div>

  <svg class="layer footer-shape" viewBox="0 0 900 150" aria-hidden="true">
    <path d="M0 14 C300 4 600 4 900 18 V150 H0 Z" fill="#a3c764"/>
  </svg>
  <svg class="layer footer-stripes" viewBox="0 0 145 80" aria-hidden="true">
    <g fill="#d8e6bd" opacity=".85">
      <polygon points="10,30 145,20 145,30 10,40"/>
      <polygon points="4,50 80,44 80,54 4,60"/>
      <polygon points="90,43 145,39 145,49 90,53"/>
      <polygon points="12,68 145,58 145,66 12,76"/>
    </g>
  </svg>

  <footer>
    <div class="layer signoff">
      <h2>Insert Signoff Here</h2>
      <p>Brenvoli Property Services Group</p>
    </div>
    <div class="layer contact">
      <div class="email">info@brenvoli.com.au</div>
      <div class="web">www.brenvoli.com.au</div>
    </div>
  </footer>

</main>
</body>
</html>
```